Flyer-Design für Ergotherapie zu Hause
schönes Design, rasche Weiterentwicklung, ist auf meine Wünsche eingegangen, sehr netter und professioneller Kontakt. Vielen Dank für Ihre Arbeit. Alles gute Weiterhin.
Zielgruppe
Ergotherapie zu Hause.
Geriatrie, Neurologie und Handtherapie Klienten
Aufgabenstellung
Es wären auch 3 Flyer möglich mit ähnlichem Design jedoch mit den drei Fachrichtungen Geriatrie, Neurologie und Handtherapie Klienten.
2x3 Seitig gefalzt A4 Quer

```html
<!DOCTYPE html>
<html lang="de">
<head>
<meta charset="utf-8">
<title>Ergotherapie bei Ihnen zu Hause – Flyer</title>
<link href="https://fonts.googleapis.com/css2?family=Open+Sans:wght@600&family=Roboto:ital,wght@0,300;0,400;0,500;1,300&display=swap" rel="stylesheet">
<style>
:root{
  --gold:#d29a35;
  --navy:#222f66;
  --stone:#cbc8bf;
  --white:#ffffff;
  --paper:#ffffff;
  --label:#222;
  --photo-a:#7d6d55;
  --photo-b:#c8b797;
  --line:#bdbdbd;
}
*{box-sizing:border-box;margin:0;padding:0}
html,body{width:1200px;height:1006px;overflow:hidden;background:var(--paper)}
body{position:relative;font-family:"Roboto",sans-serif;font-weight:300}

.page-label{position:absolute;font:italic 400 7px "Roboto",sans-serif;color:var(--label)}

.sheet{position:absolute;display:grid;grid-template-columns:repeat(3,218px);grid-template-rows:repeat(2,231.5px);border:1px solid var(--line)}
.sheet-inside{left:17px;top:27px}
.sheet-outside{left:17px;top:528px}
.fold{position:absolute;top:-4px;bottom:-4px;width:0;border-left:1px dashed var(--line);z-index:2}

.single{position:absolute;top:528px;width:218px;display:grid;grid-template-rows:231.5px 231.5px;border:1px solid var(--line)}
.single-neuro{left:717px}
.single-hand{left:957px}

.panel{position:relative;overflow:hidden}
.panel-white{background:var(--white)}
.panel-gold{background:var(--gold);color:var(--white)}
.panel-navy{background:var(--navy);color:var(--white)}
.photo{background:linear-gradient(150deg,var(--photo-b),var(--photo-a))}

.cap-circle{position:absolute;left:39px;top:-64px;width:140px;height:140px;border-radius:50%;display:flex;align-items:flex-end;justify-content:center;padding-bottom:40px;font:600 15.5px/1.05 "Open Sans",sans-serif;color:var(--white);text-align:center}
.cap-gold{background:var(--gold)}
.cap-navy{background:var(--navy)}
.cap-stone{background:var(--stone)}
.cap-circle.two-line{padding-bottom:34px}

.dot{position:absolute;border-radius:50%}
.dot-edge{left:99px;top:66px;width:20px;height:20px;background:var(--navy)}
.dot-white{left:99px;width:20px;height:20px;background:var(--white)}
.dot-cover{left:99px;top:174px;width:19px;height:19px}

.body{position:absolute;left:37px;right:37px;font-size:7.2px;line-height:1.42;text-align:justify}
.body p+p{margin-top:9px}
.text-navy{color:var(--navy)}

.quote{position:absolute;left:37px;right:37px;font-style:italic;font-size:7.4px;line-height:1.3;padding:7px 0 6px;border-top:1.5px dotted currentColor;border-bottom:1.5px dotted currentColor}

.caption{position:absolute;right:37px;width:60px;font-style:italic;font-size:4.6px;line-height:1.3;text-align:right;color:var(--white);padding-bottom:4px;border-bottom:1px dotted var(--white)}

.cover-title{position:absolute;left:0;right:0;top:116px;text-align:center}
.cover-title .main{display:block;font:400 19.5px/1 "Roboto",sans-serif;color:var(--gold);letter-spacing:.1px}
.cover-title .sub{display:block;margin-top:3px;font:300 12.5px/1 "Roboto",sans-serif;color:var(--navy);letter-spacing:.5px}

.brand-arch{position:absolute;left:39px;bottom:-65px;width:140px;height:140px;border-radius:50%;background:var(--white);text-align:center;padding-top:20px}
.brand-mark{display:block;width:14px;height:14px;margin:0 auto 6px;border-radius:50%;background:var(--navy)}
.brand-name{font:400 12px/1 "Roboto",sans-serif;letter-spacing:2.6px;color:var(--navy);padding-left:2.6px}

.portrait{position:absolute;left:74px;top:38px;width:70px;height:70px;border-radius:50%;border:4px solid var(--white);background:radial-gradient(circle at 50% 40%,#b79a86,#4f6e70)}
.rule-pair{position:absolute;top:73px;height:0;border-top:1.5px dotted var(--white)}

.contact{position:absolute;left:45px;right:45px;top:50px;text-align:center;color:var(--white)}
.contact .lead{font:400 7.6px/1.2 "Roboto",sans-serif;text-transform:uppercase;padding-bottom:10px;border-bottom:1.5px dotted var(--white)}
.contact .org{margin-top:12px;font:500 6px/1.3 "Roboto",sans-serif}
.contact .addr{margin-top:7px;font:400 6px/1.55 "Roboto",sans-serif}
.contact .tele{margin-top:7px;font:400 6px/1.45 "Roboto",sans-serif;padding-bottom:12px;border-bottom:1.5px dotted var(--white)}
</style>
</head>
<body>

<span class="page-label" style="left:24px;top:11px">Seite 2</span>
<span class="page-label" style="left:242px;top:11px">Seite 3</span>
<span class="page-label" style="left:460px;top:11px">Seite 4</span>

<section class="sheet sheet-inside">
  <span class="fold" style="left:218px"></span>
  <span class="fold" style="left:436px"></span>

  <div class="panel panel-white">
    <div class="cap-circle cap-gold">GERIATRIE</div>
    <span class="dot dot-edge"></span>
    <div class="body text-navy" style="top:102px">
      <p>Aliquip ex ea commodo consequat, puis autem vel eum iriure dolor in hendrerit in vulputate velit esse molestie.</p>
      <p>Consequat, vel illum dolore eu feugiat nulla facilisis at vero eros et accumsan et iusto odio dignissim qui blandit praesent luptatum zzril delenit augue duis dolore te feugait nulla facilisi erum est.</p>
    </div>
  </div>

  <div class="panel panel-gold">
    <div class="body" style="top:41px">
      <p>Lorem ipsum dolor sit amet, consectetuer adipiscing elit, sed diam nonummy nibh euismod tincidunt ut laoreet dolore magna aliquam erat volutpat. Ut wisi enim ad minim veniam, quis nostrud exerci tation ullamcorper suscipit lobortis nisl ut aliquip ex ea commodo consequat. Duis autem vel eum iriure dolor in hendrerit in vulputate velit esse molestie.</p>
      <p>Consequat, vel illum dolore eu feugiat nulla facilisis at vero eros et accumsan et iusto odio dignissim qui blandit praesent luptatum zzril delenit augue duis dolore te feugait nulla facilisi erum est.</p>
    </div>
  </div>

  <div class="panel photo" role="img" aria-label="Sepia-Foto: Füsse in Sandalen neben einem Klebeband-Kreuz am Boden">
    <div class="caption" style="top:172px">Lorem ipsum dolor sit amet, ad minim veniam, quis nostrud exerci</div>
  </div>

  <div class="panel panel-navy">
    <span class="dot dot-white" style="top:38px"></span>
    <div class="quote" style="top:75px">Consequat, vel illum dolore eu feugiat nulla facilisis at vero eros et accumsan et iusto odio dignissim qui blandit praesent.</div>
    <div class="body" style="top:125px">
      <p>Lorem ipsum dolor sit amet, ipstatem consectetuer adipiscing elit, sed diam nonummy nibh euismod tincidunt laoreet dolore magna consectetuer adipiscing. Lorem ipsum dolor sit amet, consectetuer adipiscing elit, sed diam nonummy nibh euismod tincidunt laoreet ipstatem.</p>
    </div>
  </div>

  <div class="panel photo" role="img" aria-label="Sepia-Foto: Person mit Rollator, Beine und Räder von nahem">
    <div class="caption" style="top:165px">Lorem ipsum dolor sit amet, ad minim veniam, quis nostrud exerci</div>
  </div>

  <div class="panel panel-gold">
    <div class="quote" style="top:41px">Consequat, vel illum dolore eu feugiat nulla facilisis at vero eros et accumsan et iusto odio dignissim qui blandit praesent.</div>
    <div class="body" style="top:91px">
      <p>Lorem ipsum dolor sit amet, consectetuer adipiscing elit, sed diam nonummy nibh euismod tincidunt est ut laoreet dolore magna aliquam erat volutpat. Ut wisi enim ad minim veniam, quis nostrud exerci tation ullamcorper suscipit lobortis nisl ut aliquip ex ea commodo consequat. Duis autem vel eum iriure dolor in hendrerit in vulputate velit esse molestie autem vel eum iriure dolor ullamcorper suscipit.</p>
    </div>
  </div>
</section>

<span class="page-label" style="left:24px;top:512px">Seite 5</span>
<span class="page-label" style="left:242px;top:512px">Seite 6</span>
<span class="page-label" style="left:460px;top:512px">Seite 1</span>

<section class="sheet sheet-outside">
  <span class="fold" style="left:218px"></span>
  <span class="fold" style="left:436px"></span>

  <div class="panel panel-gold">
    <span class="dot dot-white" style="top:38px"></span>
    <div class="quote" style="top:74px">Consequat, vel illum dolore eu feugiat nulla facilisis at vero eros et accumsan et iusto odio dignissim qui blandit praesent.</div>
    <div class="body" style="top:124px">
      <p>Lorem ipsum dolor sit amet, ipstatem consectetuer adipiscing elit, sed diam nonummy nibh euismod tincidunt laoreet dolore magna consectetuer adipiscing. Lorem ipsum dolor sit amet, consectetuer adipiscing elit, sed diam nonummy nibh euismod tincidunt laoreet ipstatem.</p>
    </div>
  </div>

  <div class="panel panel-navy">
    <span class="rule-pair" style="left:37px;width:33px"></span>
    <span class="rule-pair" style="left:148px;width:33px"></span>
    <div class="portrait" role="img" aria-label="Porträtfoto der Ergotherapeutin"></div>
    <div class="body" style="top:124px;padding-bottom:9px;border-bottom:1.5px dotted var(--white)">
      <p>Lorem ipsum dolor sit amet, ad minim veniam, quis nostrud exerci tation ullam corper estsuscipit lobortis lorem ipsum exerci tation ullamcorper est ipsum. Corper estsuscipit lobortis lorem ipsum exerci tation ullamcorper est ipsum.</p>
    </div>
  </div>

  <div class="panel panel-white">
    <div class="cap-circle cap-gold">GERIATRIE</div>
    <div class="cover-title"><span class="main">ERGOTHERAPIE</span><span class="sub">BEI IHNEN ZU HAUSE</span></div>
    <span class="dot dot-cover" style="background:var(--gold)"></span>
  </div>

  <div class="panel photo" role="img" aria-label="Sepia-Foto: Hände beim Einfädeln am Holztisch mit Stickarbeit"></div>

  <div class="panel panel-gold">
    <div class="contact">
      <div class="lead">Für weitere Fragen<br>bin ich gerne für Sie da</div>
      <div class="org">Ergotherapie Lindauer</div>
      <div class="addr">Martina Lindauer<br>Rosenhaldenweg 7<br>8280 Seefeld</div>
      <div class="tele">+41 70 000 12 34<br>info@ergotherapie-lindauer.ch<br>ergotherapie-lindauer@praxis-net.ch</div>
    </div>
  </div>

  <div class="panel photo" role="img" aria-label="Sepia-Foto: Hände legen Buchstaben in eine Schale">
    <div class="brand-arch"><span class="brand-mark"></span><span class="brand-name">LINDAUER</span></div>
  </div>
</section>

<section class="single single-neuro">
  <div class="panel panel-white">
    <div class="cap-circle cap-navy">NEUROLOGIE</div>
    <div class="cover-title"><span class="main">ERGOTHERAPIE</span><span class="sub">BEI IHNEN ZU HAUSE</span></div>
    <span class="dot dot-cover" style="background:var(--navy)"></span>
  </div>
  <div class="panel photo" role="img" aria-label="Sepia-Foto: Therapeutische Behandlung an Schulter und Rücken">
    <div class="brand-arch"><span class="brand-mark"></span><span class="brand-name">LINDAUER</span></div>
  </div>
</section>

<section class="single single-hand">
  <div class="panel panel-white">
    <div class="cap-circle cap-stone two-line">HAND<br>THERAPIE</div>
    <div class="cover-title"><span class="main">ERGOTHERAPIE</span><span class="sub">BEI IHNEN ZU HAUSE</span></div>
    <span class="dot dot-cover" style="background:var(--stone)"></span>
  </div>
  <div class="panel photo" role="img" aria-label="Sepia-Foto: Hand schreibt mit Stift eine Einkaufsliste">
    <div class="brand-arch"><span class="brand-mark"></span><span class="brand-name">LINDAUER</span></div>
  </div>
</section>

</body>
</html>
```